B2B IT project concept needs a website design for product (sales) pages

We need a website design, to attract customers to buy our services.

We dont yet have a name for our concept / if you have a great idea, feel free to be creative.

The design should communicate state of the art, professional, innovative and trustworthiness.

Technical requirements:
Format of delivery is HTML5 and CSS,.
The design is expected to be based on a well know CSS framework, like Bootstrap, or similar.

Our Concept
We are building a platform, by the means of which we can crowdsource quality inspection, from the design to delivery, to avoid the next IT disaster.

Our concept is a B2B product
Our customer base is large scale IT projects - typically public funding
The motivation for buying our product is : risk mitigation and avoiding failure (crashed, abandoned, never deployed, to full of errors, slow, dinosaurs) … see more here> http://www.bytegazette.co.uk/ctg/feature/5817394/the-10-worst-ever-government-it-projects

We define structure and guidelines. If the project follows these guidelines we guarantee delivery on deadlines
Our product is composed of the 4 steps below. Each can be purchased separately, or as a single insurance package.

The product is composed of 4 modules:
Module One: Why are we building this?
define project goals (research shows that 20% die because of this root cause)
stakeholder analysis
success criteria
minimal viable product definition
Module 2: What are we building ?
requirements specification & automated acceptance tests (research shows that 30% die because of this). Grades for req specification, and offer of help to improve. Review of req spec & grading is quite cheap (about 5.000 euro) - we see this as a sales channel
Module 3 : how are we building?
measuring during project execution
we set up measuring points in the continuous delivery process, and track that the developed product is inside quality margins (!)
module 4: navigate back on track
early warning system
warnings are deployed if irregularities are detected. failure to act on early warning voids the software delivery guarantee.

Target Market(s)

Our customer base is decision makers/sponsors of large scale IT projects - typically public funding

Industry/Entity Type

Software

Coding

Coded - Design and coding required

Number of Pages Required

1 page

Font styles to use
Sans Serif

Requirements
Must have
• Product description
• Contact form
• Packages of the service to select and inquire about
• should work on mobile platforms as well
Should not have
• payment options

```html
<!DOCTYPE html>
<html lang="en">
<head>
<meta charset="utf-8">
<title>Nordvik IT – B2B IT Products &amp; Services</title>
<link rel="stylesheet" href="https://fonts.googleapis.com/css2?family=Montserrat:wght@700&family=Open+Sans:ital,wght@0,400;0,600;0,700;1,400&family=Raleway:wght@400;500;700&display=swap">
<style>
:root{
  --red:#e31e25;
  --red-band:#d5262e;
  --red-band-dark:#b81d24;
  --ink:#2b2b2b;
  --muted:#555;
  --white:#fff;
  --footer:#262626;
  --hero-dark:#141414;
}
*{box-sizing:border-box;margin:0;padding:0}
html,body{width:944px;height:1200px;overflow:hidden}
body{position:relative;font-family:"Open Sans",Arial,sans-serif;color:var(--ink);background:var(--white)}

/* Hero */
.hero{position:absolute;left:0;top:0;width:944px;height:436px;overflow:hidden}
.hero-photo{position:absolute;inset:0;
  background:
    radial-gradient(ellipse at 55% 35%, #9d9a8e 0%, #6c6658 30%, transparent 65%),
    radial-gradient(ellipse at 85% 75%, #5b5a48 0%, transparent 45%),
    linear-gradient(180deg,#2a2824 0%,#4a4539 45%,#2b241c 80%,#1a1510 100%)}
.navbar{position:absolute;left:0;top:0;width:944px;height:60px;background:rgba(40,40,40,.55)}
.brand{position:absolute;left:77px;top:19px;display:flex;align-items:center;gap:8px;
  font-family:"Open Sans",sans-serif;font-weight:700;font-size:17px;color:var(--white)}
.brand-mark{width:14px;height:14px;border-radius:50%;background:var(--red)}
.nav-links{position:absolute;top:26px;left:362px;display:flex;gap:19px;list-style:none;
  font-family:"Open Sans",sans-serif;font-weight:600;font-size:10.5px;color:var(--white)}
.nav-links .active{color:var(--red)}
.nav-search{position:absolute;left:855px;top:27px}
.hero-title{position:absolute;left:77px;top:172px;font-family:"Montserrat",sans-serif;font-weight:700;
  font-size:22px;color:var(--white);text-shadow:0 2px 4px rgba(0,0,0,.6)}
.hero-text{position:absolute;left:77px;top:213px;width:520px;font-style:italic;font-size:11.6px;
  line-height:21.5px;color:#f2f2f2;text-shadow:0 1px 3px rgba(0,0,0,.7)}
.hero-button{position:absolute;left:78px;top:298px;width:162px;height:34px;border-radius:17px;background:var(--red);
  color:var(--white);font-weight:700;font-size:10.5px;display:flex;align-items:center;justify-content:center;letter-spacing:.2px}
.slider-controls{position:absolute;left:414px;top:373px}

/* Modules */
.modules-heading{position:absolute;top:473px;left:0;width:944px;text-align:center;
  font-family:"Raleway",sans-serif;font-weight:500;font-size:17.5px;color:var(--ink)}
.modules-heading strong{color:var(--red);font-weight:700}
.module{position:absolute;top:519px;width:186px}
.module-image{width:186px;height:132px;border:1px solid #d8d8d8;padding:3px;background:#fff}
.module-image div{width:100%;height:100%}
.module-title{margin-top:18px;margin-left:2px;font-family:"Raleway",sans-serif;font-weight:500;font-size:13px;color:var(--ink)}
.module-list{list-style:none;margin-top:10px;margin-left:2px}
.module-list li{position:relative;padding-left:18px;font-size:10px;line-height:25px;color:var(--muted)}
.module-list li.tick::before{content:"";position:absolute;left:1px;top:9px;width:8px;height:4px;
  border-left:2px solid var(--red);border-bottom:2px solid var(--red);transform:rotate(-45deg)}
.read-more{display:block;margin-top:11px;margin-left:2px;font-weight:700;font-size:9.5px;color:var(--red)}

/* Contact */
.contact{position:absolute;left:0;top:857px;width:944px;height:287px;
  background:linear-gradient(100deg,var(--red-band) 0%,#dc3038 45%,var(--red-band-dark) 100%);color:var(--white)}
.contact-title{position:absolute;top:28px;left:0;width:944px;text-align:center;font-family:"Raleway",sans-serif;
  font-size:17.5px;font-weight:400;letter-spacing:.3px}
.contact-title strong{font-weight:700}
.column-label{position:absolute;top:63px;font-family:"Raleway",sans-serif;font-weight:500;font-size:13px}
.field{position:absolute;left:78px;width:495px;background:var(--white);border:1px solid #ddd;
  font-size:9.5px;color:#555;padding:7px 12px}
.submit{position:absolute;left:508px;top:231px;width:66px;height:32px;border:2px solid var(--white);
  font-weight:700;font-size:10px;display:flex;align-items:center;justify-content:center}
.info-row{position:absolute;left:637px;display:flex;align-items:center}
.info-icon{width:29px;height:29px;border:2px solid var(--white);border-radius:50%;display:flex;align-items:center;justify-content:center;flex:none}
.info-text{position:absolute;left:63px;font-size:9.8px;line-height:19px;white-space:nowrap}

/* Footer */
.footer{position:absolute;left:0;top:1144px;width:944px;height:56px;background:var(--footer)}
.footer-brand{position:absolute;left:78px;top:18px;display:flex;align-items:center;gap:7px;
  font-weight:700;font-size:15px;color:#8e8e8e}
.footer-brand span.mark{width:12px;height:12px;border-radius:50%;background:#8e8e8e}
.copyright{position:absolute;left:0;width:944px;top:21px;text-align:center;font-size:9.5px;color:#e6e6e6}
.social{position:absolute;top:18px;display:flex;gap:12px;left:750px}
.social span{width:20px;height:20px;border-radius:4px;background:#f2f2f2}
</style>
</head>
<body>

<header class="hero">
  <div class="hero-photo" role="img" aria-label="Photograph of a rocket launch pad with gantry towers and smoke at night"></div>
  <nav class="navbar">
    <div class="brand"><span class="brand-mark"></span>NORDVIK IT</div>
    <ul class="nav-links">
      <li class="active">HOME</li><li>ABOUT US</li><li>PRODUCTS</li><li>SERVICES</li><li>SOLUTIONS</li><li>PARTNERS</li><li>CONTACT US</li>
    </ul>
    <svg class="nav-search" width="10" height="10" viewBox="0 0 10 10" aria-label="Search">
      <circle cx="4" cy="4" r="3" fill="none" stroke="#fff" stroke-width="1.6"/>
      <line x1="6.3" y1="6.3" x2="9.2" y2="9.2" stroke="#fff" stroke-width="1.8"/>
    </svg>
  </nav>
  <h1 class="hero-title">B2B IT PRODUCTS SERVICES COMPANY</h1>
  <p class="hero-text">We are building an application, by the means of which we can get&nbsp; quality inspection, from the design to delivery, to avoid the next IT disaster.The motivation for buying our product is risk mitigation and avoiding failure (crashed, abandoned, never deployed, to full of errors, slow )</p>
  <div class="hero-button">GET MORE INFORMATION</div>
  <svg class="slider-controls" width="116" height="20" viewBox="0 0 116 20" aria-label="Slide controls">
    <polyline points="9,3 3,10 9,17" fill="none" stroke="#fff" stroke-width="2"/>
    <circle cx="32" cy="10" r="6" fill="var(--red)" stroke="#fff" stroke-width="1.5"/>
    <circle cx="48" cy="10" r="6" fill="none" stroke="#fff" stroke-width="1.5"/>
    <circle cx="64" cy="10" r="6" fill="none" stroke="#fff" stroke-width="1.5"/>
    <circle cx="80" cy="10" r="6" fill="none" stroke="#fff" stroke-width="1.5"/>
    <polyline points="107,3 113,10 107,17" fill="none" stroke="#fff" stroke-width="2"/>
  </svg>
</header>

<main>
  <h2 class="modules-heading">Motivation for buying our product is <strong>Risk mitigation &amp; Avoiding failure</strong></h2>

  <section class="module" style="left:78px">
    <div class="module-image"><div role="img" aria-label="Man drawing business sketches on a wall" style="background:linear-gradient(135deg,#e4e4e2,#c9c9c6)"></div></div>
    <h3 class="module-title">Why are we building this?</h3>
    <ul class="module-list">
      <li class="tick">Define Project Goals</li><li class="tick">Stakeholder Analysis</li>
      <li class="tick">Minimal viable product definition</li><li class="tick">Success Criteria</li>
    </ul>
    <span class="read-more">READ MORE &gt;&gt;</span>
  </section>

  <section class="module" style="left:279px">
    <div class="module-image"><div role="img" aria-label="Hand touching a B2B network interface" style="background:radial-gradient(circle at 50% 45%,#d9a98a,#7a5b7a 60%,#4b3f6a)"></div></div>
    <h3 class="module-title">What are we building ?</h3>
    <ul class="module-list">
      <li class="tick">Requirements Specification</li><li class="tick">Automated Acceptance Tests</li>
      <li class="tick">Grades for req specification</li><li class="tick">Offer of help to improve</li>
    </ul>
    <span class="read-more">READ MORE &gt;&gt;</span>
  </section>

  <section class="module" style="left:480px">
    <div class="module-image"><div role="img" aria-label="Businessman sketching a city skyline" style="background:linear-gradient(90deg,#9fb5c2,#3c4750 70%,#1c1f22)"></div></div>
    <h3 class="module-title">How are we building?</h3>
    <ul class="module-list">
      <li class="tick">Measuring during project execution</li><li class="tick">Measuring points in the continuous</li>
      <li>delivery process</li><li class="tick">Track that the developed product</li>
    </ul>
    <span class="read-more">READ MORE &gt;&gt;</span>
  </section>

  <section class="module" style="left:681px">
    <div class="module-image"><div role="img" aria-label="Street map with location pins" style="background:linear-gradient(135deg,#f1ecdf,#e9e3c4 50%,#dfe8cf)"></div></div>
    <h3 class="module-title">Navigate back on track</h3>
    <ul class="module-list">
      <li class="tick">Early warning system</li><li class="tick">Warnings are deployed if</li>
      <li>irregularities are detected</li><li class="tick">Failure to act on early warning voids</li>
    </ul>
    <span class="read-more">READ MORE &gt;&gt;</span>
  </section>
</main>

<section class="contact">
  <h2 class="contact-title">CONTACT <strong>US</strong></h2>
  <h3 class="column-label" style="left:78px">CONTACT FORM</h3>
  <div class="field" style="top:91px;height:26px">NAME :</div>
  <div class="field" style="top:129px;height:26px">EMAIL :</div>
  <div class="field" style="top:167px;height:50px;padding-top:9px">MESSAGE :</div>
  <div class="submit">SUBMIT</div>

  <h3 class="column-label" style="left:637px">CONTACT INFORMATION</h3>
  <div class="info-row" style="top:98px">
    <div class="info-icon"><svg width="12" height="15" viewBox="0 0 12 15"><path d="M6 1a5 5 0 0 1 5 5c0 3.5-5 8-5 8S1 9.5 1 6a5 5 0 0 1 5-5z" fill="none" stroke="#fff" stroke-width="1.6"/><circle cx="6" cy="6" r="1.7" fill="#fff"/></svg></div>
    <div class="info-text" style="top:-6px">Nordvik IT 2240 NW<br>Harbor Lane # 300 - 112<br>Alderbrook Oregon 97999</div>
  </div>
  <div class="info-row" style="top:163px">
    <div class="info-icon"><svg width="14" height="10" viewBox="0 0 14 10"><rect x="0" y="0" width="14" height="10" rx="1.5" fill="#fff"/><polyline points="1,1.5 7,6 13,1.5" fill="none" stroke="var(--red-band)" stroke-width="1.3"/></svg></div>
    <div class="info-text" style="top:5px">info@nordvikit.example</div>
  </div>
  <div class="info-row" style="top:216px">
    <div class="info-icon"><svg width="13" height="13" viewBox="0 0 13 13"><path d="M3 1l2 3-1.3 1.4c.8 1.6 2.2 3 3.9 3.9L9 8l3 2-1 2c-5 0-10-5-10-10z" fill="none" stroke="#fff" stroke-width="1.4" stroke-linejoin="round"/></svg></div>
    <div class="info-text" style="top:5px">1 - 800 - 555 - 0142</div>
  </div>
</section>

<footer class="footer">
  <div class="footer-brand"><span class="mark"></span>NORDVIK IT</div>
  <p class="copyright">Coprights © 2016, Nordvik IT . All Rights Reserved.</p>
  <div class="social"><span></span><span></span><span></span><span></span></div>
</footer>

</body>
</html>
```